Lotus Pavilion Catering - Business Card Design

We are premium Asian Catering Company based in Melbourne. We specialize in full service sit down banquets.

Industry/Entity Type

Business

Contact Information for Business Card

Lotus Pavilion Catering
47b Carrington Rd Blackwood 3184
P: 03 9472 1538 | M: 0438 662 917
www.lotuspavilioncatering.com.au
info@lotuspavilioncatering.com.au

```html
<!DOCTYPE html>
<html lang="en">
<head>
<meta charset="utf-8">
<title>Lotus Pavilion Catering – Business Cards</title>
<link rel="stylesheet" href="https://fonts.googleapis.com/css2?family=Cinzel:wght@600&family=Quicksand:wght@500&family=Roboto:wght@400&display=swap">
<style>
  :root {
    --canvas: #ffffff;
    --charcoal: #232323;
    --paper: #ffffff;
    --frame: #1a1a1a;
    --crimson: #b5232f;
    --silver: #c4c4c4;
    --stone: #8e8e8e;
    --ink: #4a4a4a;
  }
  * { margin: 0; padding: 0; box-sizing: border-box; }
  html, body { width: 1200px; height: 900px; overflow: hidden; background: var(--canvas); }
  .stage { position: relative; width: 1200px; height: 900px; }

  .card { position: absolute; overflow: hidden; }

  /* Brand wordmark */
  .wordmark {
    display: flex; align-items: center; gap: 10px;
    font-family: "Cinzel", serif; font-weight: 600; text-align: center; line-height: 1.05;
  }
  .wordmark__dot { width: 12px; height: 12px; border-radius: 50%; background: var(--crimson); flex: none; }
  .wordmark__name { display: block; }
  .wordmark__sub { display: block; letter-spacing: 0.18em; }

  /* Portrait card */
  .card--portrait { left: 62px; top: 191px; width: 334px; height: 576px; background: var(--charcoal); }
  .card--portrait .wordmark {
    position: absolute; left: 0; right: 0; top: 190px; justify-content: center; color: var(--silver);
  }
  .card--portrait .wordmark__name { font-size: 30px; }
  .card--portrait .wordmark__sub { font-size: 20px; margin-top: 4px; }

  .tab {
    position: absolute; width: 82px; height: 82px; background: var(--crimson);
    border: 5px solid var(--paper); transform: rotate(45deg);
  }
  .card--portrait .tab { left: 32px; top: 334px; }

  .back-panel { position: absolute; background: var(--paper); border: 2px solid var(--frame); }
  .card--portrait .back-panel { left: 4px; top: 379px; width: 326px; height: 193px; }

  .turned {
    position: absolute; width: 193px; height: 322px;
    left: 64px; top: -66px; transform: rotate(90deg);
  }
  .turned .wordmark {
    position: absolute; left: 0; right: 0; top: 40px; justify-content: center; color: var(--stone);
  }
  .turned .wordmark__name { font-size: 19px; }
  .turned .wordmark__sub { font-size: 13px; }
  .turned .contact-list { position: absolute; left: 12px; bottom: 10px; }

  /* Contact list */
  .contact-list { list-style: none; font-family: "Quicksand", sans-serif; font-weight: 500; color: var(--ink); }
  .contact-list li { display: flex; align-items: flex-start; gap: 6px; font-size: 12.5px; line-height: 20px; }
  .contact-list li.contact-list__email { font-size: 9.5px; }
  .contact-list svg { width: 12px; height: 12px; flex: none; margin-top: 4px; }

  /* Landscape front */
  .card--front {
    left: 452px; top: 78px; width: 577px; height: 334px;
    border: 1px solid var(--frame);
    background: radial-gradient(ellipse 48% 52% at 50% 48%, #ffffff 55%, #e9e9e9 100%);
  }
  .card--front .wordmark {
    position: absolute; left: 0; right: 0; top: 120px; justify-content: center; color: var(--stone);
  }
  .card--front .wordmark__dot { width: 16px; height: 16px; }
  .card--front .wordmark__name { font-size: 42px; }
  .card--front .wordmark__sub { font-size: 26px; margin-top: 6px; }
  .card--front .web {
    position: absolute; left: 0; right: 0; bottom: 9px; text-align: center;
    font-family: "Roboto", sans-serif; font-size: 14px; color: var(--ink);
  }

  /* Landscape back */
  .card--back { left: 452px; top: 430px; width: 577px; height: 334px; background: var(--charcoal); }
  .card--back .upright {
    position: absolute; width: 300px; height: 120px; left: 40px; top: 107px; transform: rotate(90deg);
  }
  .card--back .upright .wordmark { justify-content: center; height: 100%; color: var(--silver); }
  .card--back .upright .wordmark__name { font-size: 32px; }
  .card--back .upright .wordmark__sub { font-size: 22px; margin-top: 4px; }
  .card--back .tab { left: 349px; top: 228px; width: 72px; height: 72px; }
  .card--back .back-panel { left: 381px; top: 3px; width: 192px; height: 328px; }
  .card--back .back-panel .wordmark {
    position: absolute; left: 0; right: 0; top: 116px; justify-content: center; color: var(--stone);
  }
  .card--back .back-panel .wordmark__dot { width: 9px; height: 9px; }
  .card--back .back-panel .wordmark__name { font-size: 17px; }
  .card--back .back-panel .wordmark__sub { font-size: 12px; }
  .card--back .contact-list { position: absolute; left: 8px; top: 224px; }
  .card--back .contact-list li { font-size: 12.5px; line-height: 21px; }
  .card--back .contact-list li.contact-list__email { font-size: 9.5px; }
</style>
</head>
<body>
<svg width="0" height="0" style="position:absolute" aria-hidden="true">
  <symbol id="icon-phone" viewBox="0 0 12 12">
    <circle cx="6" cy="6" r="5.3" fill="none" stroke="currentColor" stroke-width="1.2"/>
    <path d="M4 3.4l1 1.1-.6.8c.4.9 1 1.5 1.9 1.9l.8-.6 1.1 1-.7.9C5.6 8.3 3.7 6.4 3.4 4.2z" fill="currentColor"/>
  </symbol>
  <symbol id="icon-mail" viewBox="0 0 12 12">
    <circle cx="6" cy="6" r="5.3" fill="currentColor"/>
    <rect x="3.3" y="4" width="5.4" height="4" fill="#fff"/>
    <path d="M3.3 4L6 6.2 8.7 4" fill="none" stroke="currentColor" stroke-width=".7"/>
  </symbol>
  <symbol id="icon-home" viewBox="0 0 12 12">
    <circle cx="6" cy="6" r="5.3" fill="currentColor"/>
    <path d="M6 3.2L3.3 5.7h.9v2.8h1.3V7h1v1.5h1.3V5.7h.9z" fill="#fff"/>
  </symbol>
</svg>

<main class="stage">
  <!-- Portrait card -->
  <section class="card card--portrait" aria-label="Portrait business card">
    <div class="wordmark">
      <span class="wordmark__dot"></span>
      <span><span class="wordmark__name">LOTUS PAVILION</span><span class="wordmark__sub">CATERING</span></span>
    </div>
    <div class="tab"></div>
    <div class="back-panel">
      <div class="turned">
        <div class="wordmark">
          <span><span class="wordmark__name">LOTUS PAVILION</span><span class="wordmark__sub">CATERING</span></span>
        </div>
        <ul class="contact-list">
          <li><svg><use href="#icon-phone"/></svg>0438 662 917</li>
          <li><svg><use href="#icon-phone"/></svg>03 9472 1538</li>
          <li class="contact-list__email"><svg><use href="#icon-mail"/></svg>info@lotuspavilioncatering.com.au</li>
          <li><svg><use href="#icon-home"/></svg><span>47b Carrington Rd<br>Blackwood 3184</span></li>
        </ul>
      </div>
    </div>
  </section>

  <!-- Landscape front -->
  <section class="card card--front" aria-label="Business card front">
    <div class="wordmark">
      <span class="wordmark__dot"></span>
      <span><span class="wordmark__name">LOTUS PAVILION</span><span class="wordmark__sub">CATERING</span></span>
    </div>
    <p class="web">www.lotuspavilioncatering.com.au</p>
  </section>

  <!-- Landscape back -->
  <section class="card card--back" aria-label="Business card back">
    <div class="upright">
      <div class="wordmark">
        <span class="wordmark__dot"></span>
        <span><span class="wordmark__name">LOTUS PAVILION</span><span class="wordmark__sub">CATERING</span></span>
      </div>
    </div>
    <div class="tab"></div>
    <div class="back-panel">
      <div class="wordmark">
        <span><span class="wordmark__name">LOTUS PAVILION</span><span class="wordmark__sub">CATERING</span></span>
      </div>
      <ul class="contact-list">
        <li><svg><use href="#icon-phone"/></svg>0438 662 917</li>
        <li><svg><use href="#icon-phone"/></svg>03 9472 1538</li>
        <li class="contact-list__email"><svg><use href="#icon-mail"/></svg>info@lotuspavilioncatering.com.au</li>
        <li><svg><use href="#icon-home"/></svg><span>47b Carrington Rd<br>Blackwood 3184</span></li>
      </ul>
    </div>
  </section>
</main>
</body>
</html>
```